Company PowerPoint Presentation Template

I am looking for a business powerpoint template tailored to my company that specializes in permafrost services for the mining, transportation, and oil & gas industries. The template would be used to present project findings from studies completed for our clients. I am looking for a crisp, technical, professional business look to the template. Our business is located in North America and English is the primary language used to communicate our work. Complimentary colors associated with the business is blue (RGB, 0,112,192) or something similar in color.

```html
<!DOCTYPE html>
<html lang="en">
<head>
<meta charset="utf-8">
<title>Tundraline – Business Presentation Template</title>
<link rel="stylesheet" href="https://fonts.googleapis.com/css2?family=Montserrat:wght@400;500;600;700;800&family=Bebas+Neue&display=swap">
<style>
:root{
  --blue:#0a6fd1;
  --blue-deep:#0b4f9c;
  --navy:#131a28;
  --ink:#151515;
  --grey:#8a8d92;
  --line:#d9dbde;
  --board:#6d6f72;
  --white:#ffffff;
}
*{box-sizing:border-box;margin:0;padding:0}
html,body{width:904px;height:1200px;overflow:hidden;background:var(--board)}
body{position:relative;font-family:"Montserrat",sans-serif;color:var(--ink)}
.slide{position:absolute;width:276px;height:155px;background:var(--white);overflow:hidden;box-shadow:0 2px 5px rgba(0,0,0,.35)}
.abs{position:absolute}
.photo{position:absolute}
.logo{position:absolute;right:8px;top:6px;text-align:center;font-family:"Montserrat",sans-serif;font-weight:700;font-size:6px;letter-spacing:.6px;color:var(--ink);line-height:1}
.logo small{display:block;font-weight:500;font-size:1.9px;letter-spacing:.9px;color:var(--grey);margin-top:1px}
.logo.light{color:var(--white)}
.logo.light small{color:#d6d9de}
.foot{position:absolute;left:6px;right:6px;bottom:5px;height:6px;font-size:3.3px;font-weight:600;letter-spacing:.9px;color:var(--ink)}
.foot b{color:var(--blue);font-weight:600}
.foot::after{content:"";position:absolute;left:70px;right:8px;top:5px;border-top:.4px solid var(--ink)}
.foot .pg{position:absolute;right:0;top:2.5px;font-size:3px;font-weight:700}
.p{font-size:2.9px;line-height:1.35;color:#555;font-weight:400}
.p.w{color:#e6e8ec}
.h-sm{font-size:9px;font-weight:500;line-height:1;text-transform:uppercase}
.h-lg{font-size:12px;font-weight:800;line-height:1;color:var(--blue);text-transform:uppercase}
.blue{color:var(--blue)}
.frame-title{position:absolute;border:1px solid rgba(255,255,255,.85);color:var(--white);font-family:"Bebas Neue",sans-serif;text-align:center;line-height:.9}
.frame-title .big{font-size:28px;display:block}
.frame-title .mid{font-size:17px;display:block}
.item-t{font-size:6px;font-weight:600;color:var(--blue)}
.leg{font-size:3.4px;font-weight:600}
.dot{display:inline-block;width:3px;height:3px;border-radius:50%;margin-right:2px;vertical-align:middle}
svg text{font-family:"Montserrat",sans-serif}
</style>
</head>
<body>

<!-- 01 Cover -->
<section class="slide" style="left:31px;top:34px">
  <div class="photo" role="img" aria-label="Large mining excavator loading a haul truck at night" style="inset:0;background:radial-gradient(circle at 68% 38%,#b7852f 0,#5b4a33 22%,#2a2a2e 55%,#1b1e25 100%)"></div>
  <div class="logo light" style="left:10px;right:auto;top:10px;font-size:11px;text-align:left">TUNDRALINE<small style="font-size:3.4px;letter-spacing:1.6px">FROZEN GROUND CONSULTING</small></div>
  <div class="abs" style="left:10px;top:83px;color:#fff;font-size:8px;font-weight:500">PRESENTATION</div>
  <div class="abs" style="left:10px;top:94px;color:var(--blue);font-size:19px;font-weight:800;line-height:1">BUSINESS</div>
  <div class="abs" style="left:10px;top:114px;color:#fff;font-size:14px;font-weight:700;line-height:1">MARKETING</div>
  <div class="abs" style="left:10px;top:140px;color:#fff;font-size:4.6px;letter-spacing:1px;font-weight:600">www.<span class="blue">tundraline-example</span>.com</div>
</section>

<!-- 02 Contents -->
<section class="slide" style="left:315px;top:34px">
  <div class="logo">TUNDRALINE<small>FROZEN GROUND CONSULTING</small></div>
  <div class="abs" style="left:16px;top:8px;font-size:14px;font-weight:700">Contents</div>
  <div class="abs" style="left:16px;top:28px;width:36px;height:1.4px;background:var(--blue)"></div>
  <div class="abs" style="left:27px;top:40px;width:240px">
    <div class="abs" style="left:0;top:0"><b style="font-size:7px">1.</b></div>
    <div class="abs" style="left:12px;top:-1px;width:95px"><div class="item-t">Lorem ipsum</div><div class="p">Lorem ipsum dolor sit amet, consectetuer adipiscing elit, sed diam nonummy nibh euismod</div></div>
    <div class="abs" style="left:117px;top:0"><b style="font-size:7px">2.</b></div>
    <div class="abs" style="left:130px;top:-1px;width:95px"><div class="item-t">Lorem ipsum</div><div class="p">Lorem ipsum dolor sit amet, consectetuer adipiscing elit, sed diam nonummy nibh euismod tincid</div></div>
    <div class="abs" style="left:0;top:32px"><b style="font-size:7px">3.</b></div>
    <div class="abs" style="left:12px;top:31px;width:95px"><div class="item-t">Lorem ipsum</div><div class="p">Lorem ipsum dolor sit amet, consectetuer adipiscing elit, sed diam nonummy nibh euismod</div></div>
    <div class="abs" style="left:117px;top:32px"><b style="font-size:7px">4.</b></div>
    <div class="abs" style="left:130px;top:31px;width:95px"><div class="item-t">Lorem ipsum</div><div class="p">Lorem ipsum dolor sit amet, consectetuer adipiscing elit, sed diam nonummy nibh euismod tincid</div></div>
    <div class="abs" style="left:0;top:66px"><b style="font-size:7px">5.</b></div>
    <div class="abs" style="left:12px;top:65px;width:95px"><div class="item-t">Lorem ipsum</div><div class="p">Lorem ipsum dolor sit amet, consectetuer adipiscing elit, sed diam nonummy nibh euismod</div></div>
    <div class="abs" style="left:117px;top:66px"><b style="font-size:7px">6.</b></div>
    <div class="abs" style="left:130px;top:65px;width:95px"><div class="item-t">Lorem ipsum</div><div class="p">Lorem ipsum dolor sit amet, consectetuer adipiscing elit, sed diam nonummy nibh euismod tincid</div></div>
  </div>
  <div class="foot">www.<b>tundraline-example</b>.com<span class="pg">02</span></div>
</section>

<!-- 03 About our company -->
<section class="slide" style="left:597px;top:34px">
  <div class="photo" role="img" aria-label="Offshore oil platform at sea under a blue tint" style="inset:0;background:linear-gradient(180deg,#1c6fd0 0%,#2a79d3 50%,#1660b8 100%)"></div>
  <div class="frame-title" style="left:91px;top:35px;width:93px;height:84px;padding-top:6px"><span class="big">ABOUT</span><span class="mid">OUR</span><span class="big">COMPANY</span></div>
</section>

<!-- 04 About us company -->
<section class="slide" style="left:31px;top:198px">
  <div class="logo">TUNDRALINE<small>FROZEN GROUND CONSULTING</small></div>
  <div class="abs" style="left:16px;top:13px;width:134px;height:121px;background:var(--navy);padding:8px 7px 0">
    <div style="color:#fff;font-size:8px;font-weight:600;line-height:1">ABOUT US</div>
    <div style="color:var(--blue);font-size:13px;font-weight:700;line-height:1;margin-bottom:4px">COMPANY</div>
    <p class="p w" style="width:112px">Lorem ipsum dolor sit amet, consectetuer adipiscing elit, sed diam nonummy nibh euismod tincidunt ut laoreet dolore magna aliquam erat volutpat. Ut wisi enim ad minim veniam, quis nostrud exerci tation ullamcorper suscipit lobortis nisl ut aliquip ex ea commodo consequat. Duis autem vel eum iriure dolor in hendrerit in vulputate velit esse molestie consequat, vel illum dolore eu feugiat nulla facilisis at vero eros et accumsan et iusto odio dignissim qui blandit praesent luptatum zzril delenit augue duis dolore te feugait nulla facilisi.</p>
    <p class="p w" style="width:112px;margin-top:4px">Lorem ipsum dolor sit amet, cons ectetuer adipiscing elit, sed diam nonummy nibh euismod tincidunt ut laoreet dolore magna aliquam erat volutpat. Ut wisi enim ad minim veniam, quis nostrud exerci tation ullamcorper suscipit lobortis nisl ut aliquip ex ea commodo consequat. Lorem ipsum dolor sit amet, consecac.</p>
  </div>
  <svg class="abs" style="left:139px;top:26px" width="22" height="100" viewBox="0 0 22 100">
    <g fill="#fff" stroke="var(--navy)" stroke-width="1.2">
      <circle cx="11" cy="11" r="9.5"/><circle cx="11" cy="47" r="9.5"/><circle cx="11" cy="86" r="9.5"/>
    </g>
    <g fill="none" stroke="var(--navy)" stroke-width=".9">
      <rect x="6" y="7" width="9" height="6"/><path d="M9 16h4M11 13v3"/>
      <path d="M7 49a3 3 0 0 1 1-5 4 4 0 0 1 7 1 2.5 2.5 0 0 1 0 4z"/><path d="M11 49v3"/>
      <path d="M6 90l3-4 3 2 4-5"/><circle cx="16" cy="83" r=".9"/>
    </g>
  </svg>
  <div class="abs" style="left:166px;top:28px;width:100px"><div class="item-t">Lorem ipsum</div><div class="p">ipsum dolor sit amet, cons ectetuer adipiscing elit, sed diam nonummy nibh euismod tincidunt ut laoreet</div></div>
  <div class="abs" style="left:166px;top:64px;width:100px"><div class="item-t">Lorem ipsum</div><div class="p">ipsum dolor sit amet, cons ectetuer adipiscing elit, sed diam nonummy nibh euismod tincidunt ut laoreet dolore magna aliquam erat volutpat.</div></div>
  <div class="abs" style="left:166px;top:104px;width:100px"><div class="item-t">Lorem ipsum</div><div class="p">ipsum dolor sit amet, cons ectetuer adipiscing elit, sed diam nonummy nibh euismod tincidunt</div></div>
  <div class="foot">www.<b>tundraline-example</b>.com<span class="pg">04</span></div>
</section>

<!-- 05 Education -->
<section class="slide" style="left:315px;top:198px">
  <div class="logo">TUNDRALINE<small>FROZEN GROUND CONSULTING</small></div>
  <div class="abs h-sm" style="left:7px;top:8px;font-size:9.5px">OUR COMPANY <b class="blue" style="font-weight:700">EDUCATION</b></div>
  <svg class="abs" style="left:30px;top:38px" width="220" height="68" viewBox="0 0 220 68">
    <g fill="none" stroke="#111" stroke-width="1" stroke-dasharray="2 1.5">
      <rect x="4" y="2" width="62" height="62" rx="3"/><rect x="75" y="2" width="62" height="62" rx="3"/><rect x="146" y="2" width="62" height="62" rx="3"/>
    </g>
    <g fill="var(--blue)"><rect x="9" y="7" width="52" height="52"/><rect x="80" y="7" width="52" height="52"/><rect x="151" y="7" width="52" height="52"/></g>
    <g fill="none" stroke="#111" stroke-width="1"><path d="M66 33h9"/><path d="M137 33h9"/></g>
    <g fill="#111"><path d="M75 33l-3-2v4z"/><path d="M146 33l-3-2v4z"/></g>
    <g fill="none" stroke="#fff" stroke-width=".8">
      <path d="M32 17a3 3 0 1 1 6 0c0 2-1.5 2.5-1.5 4h-3c0-1.5-1.5-2-1.5-4z"/><path d="M33.5 23h3"/>
      <rect x="102" y="15" width="8" height="6"/><path d="M102 15l4 3 4-3"/>
      <path d="M173 14v8h8"/><path d="M174 20l3-3 2 2 3-4"/>
    </g>
    <g fill="#fff" font-weight="700" text-anchor="middle">
      <text x="35" y="31" font-size="4">IDEA</text><text x="106" y="31" font-size="4">PROMOTION</text><text x="177" y="31" font-size="4">GROWTH</text>
    </g>
    <g fill="#fff" font-size="2.6" font-weight="600" text-anchor="middle">
      <text x="35" y="36">Lorem ipsum dolor sit</text><text x="35" y="39">amet, consectetuer</text><text x="35" y="42">adipiscing elit, sed</text><text x="35" y="45">diam nonummy nibh</text>
      <text x="106" y="36">Lorem ipsum dolor sit</text><text x="106" y="39">amet, consectetuer</text><text x="106" y="42">adipiscing elit, sed</text><text x="106" y="45">diam nonummy nibh</text>
      <text x="177" y="36">Lorem ipsum dolor sit</text><text x="177" y="39">amet, consectetuer</text><text x="177" y="42">adipiscing elit, sed</text><text x="177" y="45">diam nonummy nibh</text>
    </g>
  </svg>
  <p class="abs p" style="left:26px;top:112px;width:224px;text-align:center">Lorem ipsum dolor sit amet, consectetuer adipiscing elit, sed diam nonummy nibh euismod tincidunt ut laoreet dolore magna aliquam erat volutpat. Ut wisi enim ad minim veniam, quis nostrud exerci tation ullamcorper suscipit lobortis nisl ut aliquip ex ea commodo consequat. Duis autem vel eum iriure dolor in hendrerit i</p>
  <div class="foot">www.<b>tundraline-example</b>.com<span class="pg">05</span></div>
</section>

<!-- 06 Market opportunities -->
<section class="slide" style="left:597px;top:198px">
  <div class="logo">TUNDRALINE<small>FROZEN GROUND CONSULTING</small></div>
  <div class="abs" style="left:13px;top:20px"><div class="h-sm" style="font-weight:700;font-size:10px">MARKET</div><div class="h-lg" style="font-size:10.5px">OPPORTUNITIES</div></div>
  <p class="abs p" style="left:13px;top:45px;width:104px;font-size:2.5px">Lorem ipsum dolor sit amet, consectetuer adipiscing elit, sed diam nonummy nibh euismod tincidunt ut laoreet dolore magna aliquam erat volutpat. Ut wisi enim ad minim veniam, quis nostrud exerci tation ullamcorper suscipit lobortis nisl ut aliquip ex ea commodo consequat. Duis autem vel eum iriure dolor in hendrerit i</p>
  <p class="abs p" style="left:13px;top:69px;width:104px;font-size:2.5px">Lorem ipsum dolor sit amet, consectetuer adipiscing elit, sed diam nonum-</p>
  <svg class="abs" style="left:15px;top:78px" width="100" height="60" viewBox="0 0 100 60">
    <ellipse cx="48" cy="34" rx="43" ry="21" fill="#0d1220"/>
    <ellipse cx="48" cy="29" rx="43" ry="21" fill="#151b2b"/>
    <path d="M48 8a43 21 0 0 1 35 9L63 25a20 8 0 0 0-15-4z" fill="var(--blue)"/>
    <path d="M83 17a43 21 0 0 1 3 22L64 31a20 8 0 0 0-1-6z" fill="#151b2b"/>
    <path d="M86 39a43 21 0 0 1-38 11V37a20 8 0 0 0 16-6z" fill="var(--blue)"/>
    <ellipse cx="48" cy="29" rx="19" ry="8" fill="#fff"/>
    <g fill="#fff" font-weight="700" font-size="5"><text x="10" y="32">40%</text><text x="62" y="17">20%</text><text x="72" y="32">20%</text><text x="60" y="46">20%</text></g>
  </svg>
  <div class="abs" style="left:133px;top:25px;font-size:3.3px;font-weight:600">CONSECTETUER ADIPISCING</div>
  <svg class="abs" style="left:128px;top:33px" width="140" height="70" viewBox="0 0 140 70">
    <g stroke="#c9ccd1" stroke-width=".4"><path d="M12 2h125M12 12h125M12 22h125M12 32h125M12 42h125M12 52h125M12 62h125M137 2v60"/></g>
    <path d="M12 2v60h125" fill="none" stroke="#333" stroke-width=".5"/>
    <g font-size="3.6" fill="#333" text-anchor="end"><text x="9" y="4">60</text><text x="9" y="14">50</text><text x="9" y="24">40</text><text x="9" y="34">30</text><text x="9" y="44">20</text><text x="9" y="54">10</text><text x="9" y="64">0</text></g>
    <rect x="20" y="20" width="14" height="42" fill="var(--navy)"/>
    <rect x="50" y="5" width="14" height="57" fill="var(--blue)"/>
    <rect x="81" y="47" width="14" height="15" fill="var(--navy)"/>
    <rect x="111" y="16" width="14" height="46" fill="var(--blue)"/>
    <g font-size="3.6" fill="#333" text-anchor="middle"><text x="27" y="69">JAN</text><text x="57" y="69">FEB</text><text x="88" y="69">MAR</text><text x="118" y="69">APR</text></g>
  </svg>
  <div class="abs" style="left:133px;top:114px;width:60px"><div class="leg blue"><span class="dot" style="background:var(--blue)"></span>Lorem ipsum</div><div class="p" style="font-size:2.3px">Lorem ipsum dolor sit amet, consectetuer adipiscing elit, sed diam nonummy nibh euismod tincidunt ut laoreet</div></div>
  <div class="abs" style="left:200px;top:114px;width:60px"><div class="leg"><span class="dot" style="background:var(--navy)"></span>Lorem ipsum</div><div class="p" style="font-size:2.3px">Lorem ipsum dolor sit amet, consectetuer adipiscing elit, sed diam nonummy nibh euismod tincidunt ut laoreet</div></div>
  <div class="foot">www.<b>tundraline-example</b>.com<span class="pg">06</span></div>
</section>

<!-- 07 Company overview -->
<section class="slide" style="left:31px;top:362px">
  <div class="logo">TUNDRALINE<small>FROZEN GROUND CONSULTING</small></div>
  <div class="abs" style="left:11px;top:15px"><div class="h-sm" style="font-weight:700;font-size:9.5px">COMPANY</div><div class="h-lg" style="font-size:14px">OVERVIEW</div></div>
  <p class="abs p" style="left:11px;top:43px;width:113px;font-size:2.6px">Lorem ipsum dolor sit amet, consectetuer adipiscing elit, sed diam nonummy nibh euismod tincidunt ut laoreet dolore magna aliquam erat volutpat. Ut wisi enim ad minim veniam, quis nostrud exerci tation ullamcorper suscipit lobortis nisl ut aliquip ex ea commodo consequat. Duis autem vel eum iriure dolor in hendrerit erat volutpat. Ut wisi enim ad minim veniam, quis nostrud exerci tation ullamcorper suscipit lobortis nisl ut aliquip ex ea commodo consequat. Duis autem vel eum iriure dolor in hendrerit i</p>
  <svg class="abs" style="left:5px;top:82px" width="130" height="50" viewBox="0 0 130 50">
    <g stroke="#c9ccd1" stroke-width=".4"><path d="M12 2h112M12 9h112M12 16h112M12 23h112M12 30h112M12 37h112M124 2v42"/></g>
    <path d="M12 2v42h112" fill="none" stroke="#333" stroke-width=".5"/>
    <g font-size="3.2" fill="#333" text-anchor="end"><text x="9" y="4">60</text><text x="9" y="11">50</text><text x="9" y="18">40</text><text x="9" y="25">30</text><text x="9" y="32">20</text><text x="9" y="39">10</text><text x="9" y="46">0</text></g>
    <polyline points="19,43 31,37 43,22 55,34 67,15 79,36 91,24 103,28 115,17" fill="none" stroke="var(--navy)" stroke-width=".7"/>
    <polyline points="19,34 31,40 43,27 55,11 67,22 79,30 91,24 103,22 115,38" fill="none" stroke="var(--blue)" stroke-width=".7"/>
    <g font-size="2" fill="#333" text-anchor="middle"><text x="19" y="49">TEXT 01</text><text x="31" y="49">TEXT 02</text><text x="43" y="49">TEXT 03</text><text x="55" y="49">TEXT 04</text><text x="67" y="49">TEXT 05</text><text x="79" y="49">TEXT 06</text><text x="91" y="49">TEXT 07</text><text x="103" y="49">TEXT 08</text><text x="115" y="49">TEXT 09</text></g>
  </svg>
  <svg class="abs" style="left:138px;top:24px" width="130" height="64" viewBox="0 0 130 64">
    <g stroke="#c9ccd1" stroke-width=".4"><path d="M12 2h114M12 10.5h114M12 19h114M12 27.5h114M12 36h114M12 44.5h114M126 2v51"/></g>
    <path d="M12 2v51h114" fill="none" stroke="#333" stroke-width=".5"/>
    <g font-size="3.4" fill="#333" text-anchor="end"><text x="9" y="4">60</text><text x="9" y="12.5">50</text><text x="9" y="21">40</text><text x="9" y="29.5">30</text><text x="9" y="38">20</text><text x="9" y="46.5">10</text><text x="9" y="55">0</text></g>
    <rect x="19" y="19" width="3.5" height="34" fill="var(--navy)"/><rect x="24" y="7" width="3.5" height="46" fill="var(--blue)"/>
    <rect x="43" y="43" width="3.5" height="10" fill="var(--navy)"/><rect x="48" y="23" width="3.5" height="30" fill="var(--blue)"/>
    <rect x="68" y="3" width="3.5" height="50" fill="var(--navy)"/><rect x="73" y="41" width="3.5" height="12" fill="var(--blue)"/>
    <rect x="95" y="6" width="3.5" height="47" fill="var(--blue)"/><rect x="100" y="27" width="3.5" height="26" fill="var(--navy)"/>
    <g font-size="3.4" fill="#333" text-anchor="middle"><text x="23" y="60">JAN</text><text x="48" y="60">FEB</text><text x="73" y="60">MAR</text><text x="99" y="60">APR</text></g>
  </svg>
  <div class="abs" style="left:146px;top:96px;width:55px"><div class="leg"><span class="dot" style="background:var(--navy)"></span>Lorem ipsum</div><div class="p" style="font-size:2.2px">Lorem ipsum dolor sit amet, consectetuer adipiscing elit, sed diam nonummy nibh euismod tincidunt</div></div>
  <div class="abs" style="left:208px;top:96px;width:55px"><div class="leg blue"><span class="dot" style="background:var(--blue)"></span>Lorem ipsum</div><div class="p" style="font-size:2.2px">Lorem ipsum dolor sit amet, consectetuer adipiscing elit, sed diam nonummy nibh euismod tincidunt</div></div>
  <div class="abs" style="left:146px;top:116px;width:55px"><div class="leg blue"><span class="dot" style="background:var(--blue)"></span>Lorem ipsum</div><div class="p" style="font-size:2.2px">Lorem ipsum dolor sit amet, consectetuer adipiscing elit, sed diam nonummy nibh euismod tincidunt</div></div>
  <div class="abs" style="left:208px;top:116px;width:55px"><div class="leg"><span class="dot" style="background:var(--navy)"></span>Lorem ipsum</div><div class="p" style="font-size:2.2px">Lorem ipsum dolor sit amet, consectetuer adipiscing elit, sed diam nonummy nibh euismod tincidunt</div></div>
  <div class="foot">www.<b>tundraline-example</b>.com<span class="pg">07</span></div>
</section>

<!-- 08 About our service -->
<section class="slide" style="left:315px;top:362px">
  <div class="photo" role="img" aria-label="Oil pump jacks silhouetted against a dusk sky" style="inset:0;background:linear-gradient(180deg,#3a3d44 0%,#2a2b30 55%,#18191c 100%)"></div>
  <div class="frame-title" style="left:92px;top:35px;width:93px;height:84px;padding-top:6px"><span class="big">ABOUT</span><span class="mid">OUR</span><span class="big">SERVICE</span></div>
</section>

<!-- 09 Lorem ipsum dolor sit amet (list) -->
<section class="slide" style="left:597px;top:362px">
  <div class="logo">TUNDRALINE<small>FROZEN GROUND CONSULTING</small></div>
  <div class="abs" style="left:0;top:13px;width:142px;height:121px;background:var(--navy);padding:6px 8px 0 8px">
    <div style="color:#fff;font-size:9.5px;font-weight:500;line-height:1">LOREM IPSUM</div>
    <div style="color:var(--blue);font-size:9.5px;font-weight:800;line-height:1.1;margin-bottom:4px">DOLOR SIT AMET</div>
    <ul style="list-style:none;color:#e6e8ec;font-size:3px;line-height:1.35">
      <li style="margin-bottom:4px">• <b>Lorem ipsum</b> : dolor sit amet, consectetuer adipiscing elit, nonummy nibh euismod tincidunt ut laoreet dolore magna</li>
      <li style="margin-bottom:4px">• <b>Lorem ipsum</b> : dolor sit amet, consectetuer adipiscing elit, sed diam nonummy nibh euismod tincidunt ut laoreet dolore magna aliquam erat volutpat. Ut wisi enim ad min, quis nostrud exerci tation ullamcorper suscipit lobortis nisl</li>
      <li style="margin-bottom:4px">• <b>Lorem ipsum</b> : dolor sit amet, consectetuer adipis cing elit, sed diam nonummy nibh euismod tinci dunt ut laoreet dolore magna aliquam erat volutpat.</li>
      <li style="margin-bottom:4px">• <b>Lorem ipsum</b> : dolor sit amet, consectetuer adipiscing nibh euismod tincidunt ut laoreet dolore magna</li>
      <li>• <b>Lorem ipsum</b> : dolor sit amet, consectetuer adipis cing elit, sed diam nonummy nibh euismod tinci dunt ut laoreet dolore.</li>
    </ul>
  </div>
  <div class="photo" role="img" aria-label="Yellow wheel loader on white" style="left:148px;top:28px;width:122px;height:95px;background:radial-gradient(ellipse at 50% 55%,#e6b930 0,#c89a22 30%,#f2f2f2 62%,#fff 100%)"></div>
  <div class="foot">www.<b>tundraline-example</b>.com<span class="pg">09</span></div>
</section>

<!-- 10 Active intelligence -->
<section class="slide" style="left:31px;top:524px">
  <div class="logo">TUNDRALINE<small>FROZEN GROUND CONSULTING</small></div>
  <div class="abs" style="left:17px;top:20px;width:68px;height:1.6px;background:var(--navy)"></div>
  <div class="photo" role="img" aria-label="Bucket-wheel excavator in a snowy open-pit mine" style="left:0;top:24px;width:145px;height:103px;background:linear-gradient(160deg,#d8dadd 0%,#aeb2b7 45%,#6b7077 75%,#4a4e55 100%)"></div>
  <div class="abs" style="left:148px;top:35px;width:1.6px;height:97px;background:var(--navy)"></div>
  <div class="abs" style="left:128px;top:131px;width:21px;height:1.6px;background:var(--navy)"></div>
  <div class="abs" style="left:154px;top:20px"><div class="h-sm" style="font-size:9.5px">ACTIVE</div><div class="h-lg" style="font-size:10.5px">INTELLIGENCE</div></div>
  <p class="abs p" style="left:154px;top:45px;width:110px;text-align:justify;font-size:2.6px">Lorem ipsum dolor sit amet, consectetuer adipiscing elit, sed diam nonummy nibh euismod tincidunt ut laoreet dolore magna aliquam erat volutpat. Ut wisi enim ad minim veniam, quis nostrud exerci tation ullamcorper suscipit lobortis nisl ut aliquip ex ea commodo consequat. Duis autem vel eum iriure dolor in hendrerit in vulputate velit esse</p>
  <p class="abs p" style="left:154px;top:73px;width:110px;text-align:justify;font-size:2.6px">Lorem ipsum dolor sit amet, consectetuer adipiscing elit, sed diam nonummy nibh euismod tincidunt ut laoreet dolore magna aliquam erat volutpat. Ut wisi enim ad minim veniam, quis nostrud exerci tation ullamcorper suscipit lobortis nisl ut aliquip ex ea commodo consequat. Duis autem vel eum iriure dolor in hendrerit in vulputate velit esse</p>
  <div class="abs" style="left:155px;top:108px;font-size:3px;color:var(--blue)">▶</div>
  <p class="abs p" style="left:162px;top:108px;width:102px;font-size:2.4px">Lorem ipsum dolor sit amet, consectetuer adipiscing elit, sed diam nonummy nibh euismod tincidunt ut laoreet dolore magna</p>
  <div class="abs" style="left:155px;top:122px;font-size:3px;color:var(--blue)">▷</div>
  <p class="abs p" style="left:162px;top:122px;width:102px;font-size:2.4px">Lorem ipsum dolor sit amet, consectetuer adipiscing elit, sed diam nonummy nibh euismod tincidunt ut laoreet dolore magna</p>
  <div class="foot">www.<b>tundraline-example</b>.com<span class="pg">10</span></div>
</section>

<!-- 11 Options diagram -->
<section class="slide" style="left:315px;top:524px">
  <div class="logo">TUNDRALINE<small>FROZEN GROUND CONSULTING</small></div>
  <div class="abs h-sm" style="left:11px;top:9px;font-size:9.5px">LOREM IPSUM <b class="blue" style="font-weight:700">DOLOR SIT AMET</b></div>
  <svg class="abs" style="left:0;top:0" width="276" height="155" viewBox="0 0 276 155">
    <g fill="#fff" stroke="#111" stroke-width="1.8">
      <path d="M108 66l18 20M158 66l-16 20M100 88l24 6M190 88l-22 6"/>
      <circle cx="110" cy="49" r="15"/><circle cx="156" cy="48" r="15"/><circle cx="88" cy="80" r="14"/><circle cx="186" cy="78" r="14"/>
      <circle cx="140" cy="103" r="22"/>
    </g>
    <circle cx="140" cy="103" r="17" fill="none" stroke="var(--blue)" stroke-width="5" stroke-dasharray="6 3"/>
    <circle cx="140" cy="103" r="12" fill="#fff"/>
    <text x="140" y="104" font-size="2.8" font-weight="700" text-anchor="middle">TUNDRALINE</text>
    <g fill="var(--navy)"><rect x="105" y="42" width="8" height="6"/><path d="M150 45l6-3 6 3-6 3z"/><path d="M84 75l4-2 4 2-4 2z"/><rect x="181" y="72" width="9" height="6"/></g>
    <g fill="var(--blue)"><rect x="110" y="46" width="4" height="4"/><rect x="186" y="70" width="3" height="3"/></g>
    <g font-size="3.4" font-weight="700" fill="#111" text-anchor="middle"><text x="110" y="57">Option B</text><text x="156" y="57">Option C</text><text x="86" y="88">Option A</text><text x="186" y="86">Option D</text></g>
    <g font-size="4" font-weight="700" fill="var(--blue)"><text x="125" y="36" text-anchor="end">Your Title</text><text x="173" y="35">Your Title</text><text x="72" y="65" text-anchor="end">Your Title</text><text x="203" y="66">Your Title</text></g>
    <g font-size="2.2" fill="#555">
      <text x="92" y="40" text-anchor="end">Lorem ipsum dolor sit</text><text x="92" y="43" text-anchor="end">amet, consectetuer</text><text x="92" y="46" text-anchor="end">adipiscing elit, sed diam</text><text x="92" y="49" text-anchor="end">nonummy nibh</text>
      <text x="173" y="39">Lorem ipsum dolor sit</text><text x="173" y="42">amet, consectetuer</text><text x="173" y="45">adipiscing elit, sed diam</text><text x="173" y="48">nonummy nibh</text>
      <text x="72" y="69" text-anchor="end">Lorem ipsum dolor sit</text><text x="72" y="72" text-anchor="end">amet, consectetuer</text><text x="72" y="75" text-anchor="end">adipiscing elit, sed diam</text><text x="72" y="78" text-anchor="end">nonummy nibh</text>
      <text x="203" y="70">Lorem ipsum dolor sit</text><text x="203" y="73">amet, consectetuer</text><text x="203" y="76">adipiscing elit, sed diam</text><text x="203" y="79">nonummy nibh</text>
    </g>
  </svg>
  <p class="abs p" style="left:28px;top:128px;width:220px;text-align:center;font-size:2.7px">Lorem ipsum dolor sit amet, consectetuer adipiscing elit, sed diam nonummy nibh euismod tincidunt ut laoreet dolore magna aliquam erat volutpat. Ut wisi enim ad minim veniam, quis nostrud exerci tation ullamcorper suscipit lobortis nisl ut aliquip ex ea commodo consequat. Duis autem vel eum iriure dolor in hendrerit i</p>
  <div class="foot">www.<b>tundraline-example</b>.com<span class="pg">11</span></div>
</section>

<!-- 12 Benefits to each customer segments -->
<section class="slide" style="left:597px;top:524px">
  <div class="logo">TUNDRALINE<small>FROZEN GROUND CONSULTING</small></div>
  <div class="abs" style="left:15px;top:18px"><div class="h-sm" style="font-size:9.5px">BENEFITS TO EACH</div><div class="h-lg" style="font-size:10.5px">CUSTOMER SEGMENTS</div></div>
  <div class="abs" style="left:15px;top:45px;width:123px">
    <p class="p" style="font-size:2.6px;margin-bottom:3px">Lorem ipsum dolor sit amet, consectetuer adipiscing elit, sed diam nonummy nibh euismod tincidunt ut laoreet dolore magna aliquam erat volutpat. Ut wisi enim ad minim veniam, quis nostrud exerci tation ullam</p>
    <p class="p" style="font-size:2.6px;margin-bottom:3px">Lorem ipsum dolor sit amet, consectetuer adipiscing elit, sed diam nonummy nibh euismod tincidunt ut laoreet dolore magna aliquam erat volutpat. Ut wisi enim ad minim veniam, quis nostrud exerci tation ullam</p>
    <p class="p" style="font-size:2.6px;margin-bottom:3px">Lorem ipsum dolor sit amet, consectetuer adipiscing elit, sed diam nonummy nibh euismod tincidunt ut laoreet dolore magna aliquam erat volutpat. Ut wisi enim ad minim veniam, quis nostrud exerci</p>
    <p class="p" style="font-size:2.6px">Lorem ipsum dolor sit amet, consectetuer adipiscing elit, sed diam nonummy nibh euismod tincidunt ut laoreet dolore magna aliquam erat volutpat. Ut wisi enim ad minim veniam, quis nostrud exerci tation ullam. Lorem ipsum dolor sit amet, consectetuer adipiscing elit, sed diam nonummy nibh euismod tincidunt ut laoreet dolore magna erat volutpat. Ut wisi enim ad minim veniam, quis nostrud exerci</p>
  </div>
  <div class="abs" style="left:152px;top:27px;width:15px;height:15px;background:var(--blue)"></div>
  <div class="photo" role="img" aria-label="Refinery towers at dusk" style="left:158px;top:33px;width:104px;height:98px;background:linear-gradient(180deg,#b9ad98 0%,#8d8577 45%,#4b4f55 75%,#2f3439 100%)"></div>
  <div class="foot">www.<b>tundraline-example</b>.com<span class="pg">12</span></div>
</section>

<!-- 13 About our project -->
<section class="slide" style="left:31px;top:686px">
  <div class="photo" role="img" aria-label="Aerial view of an industrial plant under a blue tint" style="inset:0;background:linear-gradient(180deg,#2a6dc0 0%,#1c5eb0 50%,#144d95 100%)"></div>
  <div class="frame-title" style="left:92px;top:36px;width:93px;height:84px;padding-top:6px"><span class="big">ABOUT</span><span class="mid">OUR</span><span class="big">PROJECT</span></div>
</section>

<!-- 14 Lorem ipsum project -->
<section class="slide" style="left:315px;top:686px">
  <div class="logo">TUNDRALINE<small>FROZEN GROUND CONSULTING</small></div>
  <div class="abs h-sm" style="left:0;right:0;top:22px;text-align:center;font-size:10.5px">LOREM IPSUM <b class="blue" style="font-weight:700">PROJECT</b></div>
  <p class="abs p" style="left:22px;top:37px;width:232px;text-align:center;font-size:2.6px">Lorem ipsum dolor sit amet, consectetuer adipiscing elit, sed diam nonummy nibh euismod tincidunt ut laoreet dolore magna aliquam erat volutpat. Ut wisi enim ad minim veniam, quis nostrud exerci tation ullamcorper suscipit lobortis nisl utea commodo consequat. Duis autem vel eum iriure dolor in hendrerit i</p>
  <p class="abs p" style="left:22px;top:55px;width:232px;text-align:center;font-size:2.6px">Lorem ipsum dolor sit amet, consectetuer adipiscing elit, sed diam nonummy nibh m ipsum dolor sit amet, consectetuer adipiscing elit, sed diam nonummy nibh euismod tincidunt ut laoreet dolore magna.</p>
  <div class="photo" role="img" aria-label="Excavator at a mine site" style="left:11px;top:71px;width:59px;height:40px;background:linear-gradient(160deg,#6e6658,#3e3a33 60%,#a47c3c);border:1px solid #ccc"></div>
  <div class="photo" role="img" aria-label="Drilling rig in a tunnel" style="left:76px;top:71px;width:59px;height:40px;background:linear-gradient(160deg,#5b5653,#a2412d 55%,#3a3634);border:1px solid #ccc"></div>
  <div class="photo" role="img" aria-label="Offshore platform under a dramatic sky" style="left:141px;top:71px;width:59px;height:40px;background:linear-gradient(180deg,#3b5e93,#8aa4c4 50%,#233a5c);border:1px solid #ccc"></div>
  <div class="photo" role="img" aria-label="Refinery pipework at sunset" style="left:206px;top:71px;width:59px;height:40px;background:linear-gradient(180deg,#d6b98a,#9c7f58 50%,#3f3b36);border:1px solid #ccc"></div>
  <div class="abs" style="left:11px;top:114px;width:59px"><div class="item-t" style="font-size:5px">Lorem ipsum</div><div class="p" style="font-size:2.2px">Lorem ipsum dolor sit amet, consectetuer adipiscing elit, sed diam nonummy nibh euismod tincidunt ut laoreet</div></div>
  <div class="abs" style="left:76px;top:114px;width:59px"><div class="item-t" style="font-size:5px">Lorem ipsum</div><div class="p" style="font-size:2.2px">Lorem ipsum dolor sit amet, consectetuer adipiscing elit, sed diam nonummy nibh euismod tincidunt ut laoreet</div></div>
  <div class="abs" style="left:141px;top:114px;width:59px"><div class="item-t" style="font-size:5px">Lorem ipsum</div><div class="p" style="font-size:2.2px">Lorem ipsum dolor sit amet, consectetuer adipiscing elit, sed diam nonummy nibh euismod tincidunt ut laoreet</div></div>
  <div class="abs" style="left:206px;top:114px;width:59px"><div class="item-t" style="font-size:5px">Lorem ipsum</div><div class="p" style="font-size:2.2px">Lorem ipsum dolor sit amet, consectetuer adipiscing elit, sed diam nonummy nibh euismod tincidunt ut laoreet</div></div>
  <div class="foot">www.<b>tundraline-example</b>.com<span class="pg">14</span></div>
</section>

<!-- 15 Portfolio of projects -->
<section class="slide" style="left:597px;top:686px">
  <div class="logo">TUNDRALINE<small>FROZEN GROUND CONSULTING</small></div>
  <div class="abs" style="left:13px;top:24px;width:103px;height:103px;border:.8px solid #333"></div>
  <div class="photo" role="img" aria-label="Offshore oil rig at sea in soft light" style="left:16px;top:27px;width:97px;height:97px;background:linear-gradient(180deg,#c9cbcf 0%,#a9aeb5 45%,#5d6a78 70%,#3d4957 100%)"></div>
  <div class="abs" style="left:125px;top:25px"><div class="h-sm" style="font-size:7px">PORTFOLIO OF</div><div class="h-lg" style="font-size:14px">PROJECTS</div></div>
  <p class="abs p" style="left:125px;top:49px;width:138px;font-size:2.6px">Lorem ipsum dolor sit amet, consectetuer adipiscing elit, sed diam nonummy nibh euismod tincidunt ut laoreet dolore magna aliquam erat volutpat. Ut wisi enim ad minim veniam, quis nostrud exerci tation ullamcorper suscipit lobortis nisl ut aliquip ex ea commodo consequat. Duis autem vel eum iriure dolor in hendrerit in vulputate velit esse</p>
  <p class="abs p" style="left:125px;top:77px;width:138px;font-size:2.6px">Lorem ipsum dolor sit amet, consectetuer adipiscing elit, sed diam nonummy nibh euismod tincidunt ut laoreet dolore magna aliquam erat volutpat. Ut wisi enim ad minim veniam, quis nostrud exerci tation ullamcorper suscipit lobortis nisl ut aliquip ex ea commodo consequat. Duis autem vel eum iriure dolor in hendrerit in vulputate velit esse</p>
  <div class="abs" style="left:126px;top:101px;font-size:3.4px;color:var(--blue)">▶</div>
  <p class="abs p" style="left:134px;top:101px;width:128px;font-size:2.4px">Lorem ipsum dolor sit amet, consectetuer adipiscing elit, sed diam nonummy nibh euismod tincidunt ut laoreet dolore magna</p>
  <div class="abs" style="left:126px;top:119px;font-size:3.4px;color:var(--blue)">▷</div>
  <p class="abs p" style="left:134px;top:119px;width:128px;font-size:2.4px">Lorem ipsum dolor sit amet, consectetuer adipiscing elit, sed diam nonummy nibh euismod tincidunt ut laoreet dolore magna</p>
  <div class="foot">www.<b>tundraline-example</b>.com<span class="pg">15</span></div>
</section>

<!-- 16 Timeline roadmap -->
<section class="slide" style="left:31px;top:848px">
  <div class="logo">TUNDRALINE<small>FROZEN GROUND CONSULTING</small></div>
  <svg class="abs" style="left:0;top:0" width="276" height="155" viewBox="0 0 276 155">
    <path d="M238 93V128H150C128 128 126 100 150 96S180 88 171 80S150 70 128 62S96 46 106 42S136 38 128 30S100 20 88 26" fill="none" stroke="#111" stroke-width="1.4"/>
    <g stroke="var(--blue)" stroke-width=".8" stroke-dasharray="1.5 1.5" fill="none"><path d="M238 93v35"/><path d="M156 62v42"/><path d="M200 50v16"/></g>
    <circle cx="238" cy="128" r="1.5" fill="var(--blue)"/>
    <circle cx="238" cy="71" r="19" fill="var(--blue)"/><circle cx="238" cy="71" r="15" fill="#fff"/>
    <path d="M231 88l7 7 7-7z" fill="var(--blue)"/>
    <text x="238" y="79" font-size="22" font-weight="700" text-anchor="middle">1</text>
    <circle cx="143" cy="55" r="10" fill="var(--blue)"/><circle cx="143" cy="55" r="7.5" fill="#fff"/><text x="143" y="59.5" font-size="11" font-weight="700" text-anchor="middle">2</text>
    <circle cx="185" cy="37" r="9" fill="var(--blue)"/><circle cx="185" cy="37" r="6.8" fill="#fff"/><text x="185" y="41" font-size="10" font-weight="700" text-anchor="middle">3</text>
    <circle cx="106" cy="37" r="6" fill="var(--blue)"/><circle cx="106" cy="37" r="4.5" fill="#fff"/><text x="106" y="40" font-size="7" font-weight="700" text-anchor="middle">4</text>
    <circle cx="128" cy="27" r="5" fill="var(--blue)"/><circle cx="128" cy="27" r="3.7" fill="#fff"/><text x="128" y="29.5" font-size="6" font-weight="700" text-anchor="middle">5</text>
    <circle cx="88" cy="25" r="3.5" fill="var(--blue)"/><circle cx="88" cy="25" r="2.5" fill="#fff"/><text x="88" y="26.5" font-size="3.6" font-weight="700" text-anchor="middle">6</text>
    <g font-size="4" font-weight="600"><text x="50" y="27">Lorem ipsum</text><text x="150" y="22">Lorem ipsum</text><text x="212" y="25">Lorem ipsum</text><text x="112" y="64">Lorem ipsum</text><text x="200" y="94">Lorem ipsum</text></g>
    <g font-size="2" fill="#666">
      <text x="50" y="30">Lorem ipsum dolor sit amet,</text><text x="50" y="32.5">consectetuer adipiscing elit,</text><text x="50" y="35">sed diam nonummy nibh</text>
      <text x="150" y="25">Lorem ipsum dolor sit amet,</text><text x="150" y="27.5">consectetuer adipiscing elit,</text><text x="150" y="30">sed diam nonummy nibh</text>
      <text x="212" y="28">Lorem ipsum dolor sit amet,</text><text x="212" y="30.5">consectetuer adipiscing elit,</text><text x="212" y="33">sed diam nonummy nibh</text>
      <text x="112" y="67">Lorem ipsum dolor sit amet,</text><text x="112" y="69.5">consectetuer adipiscing elit,</text><text x="112" y="72">sed diam nonummy nibh</text>
      <text x="200" y="97">Lorem ipsum dolor sit amet,</text><text x="200" y="99.5">consectetuer adipiscing elit,</text><text x="200" y="102">sed diam nonummy nibh</text>
    </g>
    <circle cx="24" cy="127" r="7" fill="var(--navy)"/><text x="24" y="130" font-size="8" font-weight="700" fill="#fff" text-anchor="middle">A</text>
    <circle cx="86" cy="127" r="7" fill="var(--navy)"/><text x="86" y="130" font-size="8" font-weight="700" fill="#fff" text-anchor="middle">B</text>
    <g font-size="7" font-weight="600" fill="var(--blue)"><text x="34" y="124">2019</text><text x="96" y="124">2020</text></g>
    <g font-size="2" fill="#666"><text x="34" y="128">Lorem ipsum dolor sit</text><text x="34" y="130.5">amet, consectetuer</text><text x="34" y="133">adipiscing elit, sed diam</text>
      <text x="96" y="128">Lorem ipsum dolor sit</text><text x="96" y="130.5">amet, consectetuer</text><text x="96" y="133">adipiscing elit, sed diam</text></g>
  </svg>
  <div class="abs" style="left:16px;top:79px;font-size:5px;font-weight:500;letter-spacing:.8px;color:var(--blue)">TIMELINE OF</div>
  <div class="abs" style="left:16px;top:85px;font-size:13px;font-weight:800;line-height:1">ROADMAP</div>
  <div class="abs" style="left:16px;top:99px;font-size:6px;font-weight:700;color:var(--blue)">FOR 2 YEARS</div>
  <div class="foot">www.<b>tundraline-example</b>.com<span class="pg">16</span></div>
</section>

<!-- 17 Company summary -->
<section class="slide" style="left:315px;top:848px">
  <div class="logo">TUNDRALINE<small>FROZEN GROUND CONSULTING</small></div>
  <div class="abs h-sm" style="left:17px;top:17px;font-size:9px">COMPANY <b class="blue" style="font-weight:800;font-size:12px">SUMMARY</b></div>
  <div class="abs" style="left:17px;top:35px;width:101px;height:15px;background:#8c8c8c"></div>
  <div class="abs" style="left:17px;top:64px;width:75px"><div class="leg blue" style="font-size:4.5px"><span class="dot" style="background:var(--navy);width:4px;height:4px;margin-right:5px"></span>Lorem ipsum</div><div class="p" style="font-size:2.4px;padding-left:9px">Lorem ipsum dolor sit amet, consectetuer adipiscing elit, sed diam nonummy nibh euismod tincidunt</div></div>
  <div class="abs" style="left:17px;top:88px;width:75px"><div class="leg blue" style="font-size:4.5px"><span class="dot" style="background:var(--navy);width:4px;height:4px;margin-right:5px"></span>Lorem ipsum</div><div class="p" style="font-size:2.4px;padding-left:9px">Lorem ipsum dolor sit amet, consectetuer adipiscing elit, sed diam nonummy nibh euismod tincidunt</div></div>
  <div class="abs" style="left:17px;top:112px;width:75px"><div class="leg blue" style="font-size:4.5px"><span class="dot" style="background:var(--navy);width:4px;height:4px;margin-right:5px"></span>Lorem ipsum</div><div class="p" style="font-size:2.4px;padding-left:9px">Lorem ipsum dolor sit amet, consectetuer adipiscing elit, sed diam nonummy nibh euismod tincidunt</div></div>
  <svg class="abs" style="left:0;top:0" width="276" height="155" viewBox="0 0 276 155">
    <path d="M200 40A45 45 0 1 1 130 100" fill="none" stroke="#111" stroke-width="1.6"/>
    <path d="M196 38A45 45 0 0 0 123 78" fill="none" stroke="#111" stroke-width="1.6"/>
    <path d="M119 74l4 7 4-7z" fill="#111"/>
    <circle cx="128" cy="97" r="2" fill="#111"/>
    <circle cx="208" cy="48" r="13" fill="#fff" stroke="var(--blue)" stroke-width="2.5"/><circle cx="208" cy="48" r="9" fill="var(--blue)"/><circle cx="208" cy="48" r="3" fill="none" stroke="#fff" stroke-width="1"/>
    <circle cx="218" cy="88" r="8.5" fill="#fff" stroke="var(--blue)" stroke-width="2"/><circle cx="218" cy="88" r="5.5" fill="var(--blue)"/>
    <circle cx="197" cy="126" r="6" fill="#fff" stroke="var(--blue)" stroke-width="1.6"/><circle cx="197" cy="126" r="3.8" fill="var(--blue)"/>
    <circle cx="150" cy="110" r="5.5" fill="#fff" stroke="var(--blue)" stroke-width="1.6"/><circle cx="150" cy="110" r="3.4" fill="var(--blue)"/>
    <g fill="var(--navy)"><rect x="151" y="66" width="2" height="7"/><rect x="154" y="63" width="2" height="10"/><rect x="157" y="68" width="2" height="5"/><rect x="160" y="65" width="2" height="8"/></g>
    <text x="156" y="79" font-size="3.6" font-weight="700" text-anchor="middle">Main Title</text>
    <g font-size="2" fill="#666" text-anchor="middle"><text x="156" y="82">Lorem ipsum dolor sit amet,</text><text x="156" y="84.5">consectetuer adipiscing elit,</text><text x="156" y="87">sed diam nonummy nibh</text></g>
    <g font-size="3" font-weight="700"><text x="222" y="38">85%</text><text x="191" y="85">80%</text><text x="158" y="107">50%</text><text x="203" y="138">75%</text></g>
    <g fill="none" stroke="var(--blue)" stroke-width=".6"><path d="M214 38h7M206 86h-7M199 132l4 4"/></g>
    <g font-size="3.8" font-weight="700"><text x="245" y="49" text-anchor="end">Your Title</text><text x="257" y="91" text-anchor="end">Your Title</text><text x="138" y="104" text-anchor="end">Your Title</text><text x="255" y="121" text-anchor="end">Your Title</text></g>
    <g font-size="2" fill="#666" text-anchor="end">
      <text x="245" y="52">Lorem ipsum dolor sit amet,</text><text x="245" y="54.5">consectetuer adipiscing elit,</text><text x="245" y="57">sed diam nonummy nibh</text>
      <text x="257" y="94">Lorem ipsum dolor sit amet,</text><text x="257" y="96.5">consectetuer adipiscing elit,</text><text x="257" y="99">sed diam nonummy nibh</text>
      <text x="138" y="107">Lorem ipsum dolor sit amet,</text><text x="138" y="109.5">consectetuer adipiscing elit,</text><text x="138" y="112">sed diam nonummy nibh</text>
      <text x="255" y="124">Lorem ipsum dolor sit amet,</text><text x="255" y="126.5">consectetuer adipiscing elit,</text><text x="255" y="129">sed diam nonummy nibh</text>
    </g>
  </svg>
  <div class="foot">www.<b>tundraline-example</b>.com<span class="pg">17</span></div>
</section>

<!-- 18 Starting new section -->
<section class="slide" style="left:597px;top:848px">
  <div class="logo">TUNDRALINE<small>FROZEN GROUND CONSULTING</small></div>
  <div class="abs" style="left:12px;top:8px"><div class="h-sm" style="font-size:10px">STARTING</div><div class="h-lg" style="font-size:12.5px">NEW SECTION</div></div>
  <div class="photo" role="img" aria-label="Isometric staircase of blue and navy blocks rising to an upward arrow, labelled Step 01 to Step 04" style="left:106px;top:20px;width:82px;height:130px;background:linear-gradient(200deg,#131a28 0%,#1b2a44 45%,#0b55a8 80%,#0a6fd1 100%)"></div>
  <svg class="abs" style="left:0;top:0" width="276" height="155" viewBox="0 0 276 155">
    <rect x="56" y="53" width="50" height="13" fill="var(--navy)"/>
    <rect x="46" y="69" width="60" height="13" fill="var(--blue)"/>
    <rect x="36" y="85" width="70" height="13" fill="var(--navy)"/>
    <rect x="24" y="101" width="82" height="13" fill="var(--blue)"/>
    <g fill="#fff" font-weight="800" font-size="7"><text x="58" y="62">50%</text><text x="48" y="78">40%</text><text x="38" y="94">30%</text><text x="26" y="110">20%</text></g>
    <g stroke="#fff" stroke-width=".4"><path d="M75 55v9M65 71v9M55 87v9M43 103v9"/></g>
    <g fill="#fff" font-size="1.9"><text x="77" y="58">Lorem ipsum dolor sit amet,</text><text x="77" y="60.5">consectetuer adipiscing elit</text>
      <text x="67" y="74">Lorem ipsum dolor sit amet,</text><text x="67" y="76.5">consectetuer adipiscing elit</text>
      <text x="57" y="90">Lorem ipsum dolor sit amet,</text><text x="57" y="92.5">consectetuer adipiscing elit</text>
      <text x="45" y="106">Lorem ipsum dolor sit amet,</text><text x="45" y="108.5">consectetuer adipiscing elit</text></g>
  </svg>
  <div class="abs" style="left:197px;top:33px;width:70px">
    <div style="margin-bottom:8px"><div class="leg" style="font-size:3.6px"><span class="dot" style="background:var(--navy)"></span>Lorem ipsum</div><div class="p" style="font-size:2.1px;padding-left:5px">Lorem ipsum dolor sit amet, consectetuer adipiscing elit, sed diam nonummy nibh euismod tincidunt ut laoreet</div></div>
    <div style="margin-bottom:8px"><div class="leg blue" style="font-size:3.6px"><span class="dot" style="background:var(--blue)"></span>Lorem ipsum</div><div class="p" style="font-size:2.1px;padding-left:5px">Lorem ipsum dolor sit amet, consectetuer adipiscing elit, sed diam nonummy nibh euismod tincidunt ut laoreet</div></div>
    <div style="margin-bottom:8px"><div class="leg" style="font-size:3.6px"><span class="dot" style="background:var(--navy)"></span>Lorem ipsum</div><div class="p" style="font-size:2.1px;padding-left:5px">Lorem ipsum dolor sit amet, consectetuer adipiscing elit, sed diam nonummy nibh euismod tincidunt ut laoreet</div></div>
    <div><div class="leg blue" style="font-size:3.6px"><span class="dot" style="background:var(--blue)"></span>Lorem ipsum</div><div class="p" style="font-size:2.1px;padding-left:5px">Lorem ipsum dolor sit amet, consectetuer adipiscing elit, sed diam nonummy nibh euismod tincidunt ut laoreet</div></div>
  </div>
  <div class="foot">www.<b>tundraline-example</b>.com<span class="pg">18</span></div>
</section>

<!-- 19 Use cases -->
<section class="slide" style="left:31px;top:1011px">
  <div class="logo">TUNDRALINE<small>FROZEN GROUND CONSULTING</small></div>
  <div class="abs" style="left:16px;top:15px;width:34px;height:62px;border:1.2px solid #111;border-radius:4px;padding:12px 3px 0;box-shadow:1px 2px 3px rgba(0,0,0,.25)">
    <div style="font-size:3.8px;font-weight:500;line-height:1.1">Lorem ipsum dolor</div>
    <div style="margin:3px auto;width:6px;height:5px;border:.6px solid var(--blue)"></div>
    <div class="p" style="font-size:1.8px">To introduce the students to the changing landscape of marketing and equip them with knowledge and the tools to navigate the field.</div>
  </div>
  <div class="abs" style="left:58px;top:37px;width:34px;height:70px;border:1.2px solid #111;border-radius:4px;padding:12px 3px 0;box-shadow:1px 2px 3px rgba(0,0,0,.25)">
    <div style="font-size:3.8px;font-weight:500;line-height:1.1">Dolor sit amet, conse</div>
    <div style="margin:3px auto;width:6px;height:5px;border:.6px solid var(--blue);border-radius:50%"></div>
    <div class="p" style="font-size:1.8px">You will learn concepts and ideas in marketing as well as how to use different tools and strategies to optimize your campaigns.</div>
  </div>
  <div class="abs" style="left:101px;top:60px;width:34px;height:70px;border:1.2px solid #111;border-radius:4px;padding:12px 3px 0;box-shadow:1px 2px 3px rgba(0,0,0,.25)">
    <div style="font-size:3.8px;font-weight:500;line-height:1.1">Consec</div>
    <div style="font-size:3px;color:#888">• • • • • •</div>
    <div style="margin:3px auto;width:6px;height:5px;border:.6px solid var(--blue);border-radius:50%"></div>
    <div class="p" style="font-size:1.8px">You are required to pass 80% of the evaluation test to obtain the certificate. The test can only be taken 3 times.</div>
  </div>
  <div class="abs" style="left:148px;top:40px;font-size:16px;font-weight:500;line-height:1">USE <b class="blue" style="font-weight:700">CASES</b></div>
  <p class="abs p" style="left:148px;top:60px;width:115px;font-size:2.8px">Lorem ipsum dolor sit amet, consectetuer adipiscing elit, sed diam nonummy nibh euismod tincidunt ut laoreet dolore magna aliquam erat volutpat. Ut wisi enim ad minim veniam, quis nostrud exerci tation ullamcorper suscipit lobortis nisl ut aliquip ex ea commodo consequat. Duis autem vel eum iriure dolor in hendrerit i</p>
  <p class="abs p" style="left:148px;top:92px;width:115px;font-size:2.8px">Lorem ipsum dolor sit amet, consectetuer adipiscing elit, sed diam nonummy nibh euismod tincidunt ut laoreet dolore magna aliquam erat volutpat. Ut wisi enim ad minim veniam, quis nostrud exerci tation ullamcorper suscipit lobortis nisl ut aliquip ex ea commodo consequat. Duis autem vel eum iriure dolor in hendrerit in</p>
  <div class="foot">www.<b>tundraline-example</b>.com<span class="pg">19</span></div>
</section>

<!-- 20 Team members and advisors -->
<section class="slide" style="left:315px;top:1011px">
  <div class="logo">TUNDRALINE<small>FROZEN GROUND CONSULTING</small></div>
  <div class="abs h-sm" style="left:0;right:0;top:25px;text-align:center;font-size:8.5px">TEAM MEMBERS <b class="blue" style="font-weight:700">AND ADVISORS</b></div>
  <p class="abs p" style="left:25px;top:37px;width:226px;text-align:center;font-size:2.6px">Lorem ipsum dolor sit amet, consectetuer adipiscing elit, sed diam nonummy nibh euismod tincidunt ut laoreet dolore magna aliquam erat volutpat. Ut wisi enim ad minim veniam, quis nostrud exerci tation ullamcorper suscipit lobortis nisl ut aliquip ex ea commodo consequat. Duis autem</p>
  <p class="abs p" style="left:25px;top:52px;width:226px;text-align:center;font-size:2.6px">Lorem ipsum dolor sit amet, cons ectetuer adipiscing elit, sed diam nonummy nibh euismod tincidunt ut laoreet dolore magna aliquam erat volutpat.</p>
  <div class="abs" style="left:0;top:65px;width:276px;height:64px;background:var(--navy)"></div>
  <div class="abs" style="left:0;top:71px;width:276px;display:flex;justify-content:space-around;padding:0 8px">
    <div style="width:52px;text-align:center"><div role="img" aria-label="Team member portrait" style="width:22px;height:22px;margin:0 auto;border-radius:50%;border:1.5px solid var(--blue);background:#9aa3ad"></div><div style="color:var(--blue);font-size:4.2px;font-weight:700;margin-top:4px">AARON VALE</div><div class="p w" style="font-size:1.9px">Lorem ipsum dolor sit amet, cons ectetuer adipiscing elit, sed diam nonummy nibh euismod tincidunt ut laoreet dolore magna aliquam erat volutpat. Ut wisi enim ad minim veniam, quis nostrud</div></div>
    <div style="width:52px;text-align:center"><div role="img" aria-label="Team member portrait" style="width:22px;height:22px;margin:0 auto;border-radius:50%;border:1.5px solid var(--blue);background:#9aa3ad"></div><div style="color:var(--blue);font-size:4.2px;font-weight:700;margin-top:4px">NORA PIKE</div><div class="p w" style="font-size:1.9px">Lorem ipsum dolor sit amet, cons ectetuer adipiscing elit, sed diam nonummy nibh euismod tincidunt ut laoreet dolore magna aliquam erat volutpat. Ut wisi enim ad minim veniam, quis nostrud</div></div>
    <div style="width:52px;text-align:center"><div role="img" aria-label="Team member portrait" style="width:22px;height:22px;margin:0 auto;border-radius:50%;border:1.5px solid var(--blue);background:#9aa3ad"></div><div style="color:var(--blue);font-size:4.2px;font-weight:700;margin-top:4px">AARON VALE</div><div class="p w" style="font-size:1.9px">Lorem ipsum dolor sit amet, cons ectetuer adipiscing elit, sed diam nonummy nibh euismod tincidunt ut laoreet dolore magna aliquam erat volutpat. Ut wisi enim ad minim veniam, quis nostrud</div></div>
    <div style="width:52px;text-align:center"><div role="img" aria-label="Team member portrait" style="width:22px;height:22px;margin:0 auto;border-radius:50%;border:1.5px solid var(--blue);background:#9aa3ad"></div><div style="color:var(--blue);font-size:4.2px;font-weight:700;margin-top:4px">NORA PIKE</div><div class="p w" style="font-size:1.9px">Lorem ipsum dolor sit amet, cons ectetuer adipiscing elit, sed diam nonummy nibh euismod tincidunt ut laoreet dolore magna aliquam erat volutpat. Ut wisi enim ad minim veniam, quis nostrud</div></div>
  </div>
  <div class="foot">www.<b>tundraline-example</b>.com<span class="pg">20</span></div>
</section>

<!-- 21 Thank you -->
<section class="slide" style="left:597px;top:1011px">
  <div class="photo" role="img" aria-label="Mining haul truck with headlights on in a dark pit" style="inset:0;background:radial-gradient(circle at 80% 55%,#a57a33 0,#5a4a34 22%,#2a2b30 55%,#1a1c22 100%)"></div>
  <div class="abs" style="left:11px;top:16px;color:#fff;font-family:'Bebas Neue',sans-serif;font-size:30px;line-height:1">THANK YOU</div>
  <div class="abs" style="left:11px;top:50px;color:#fff;font-size:8.5px;font-weight:500">CONTACT <b>US</b></div>
  <div class="abs" style="left:11px;top:63px;color:#fff;font-size:5.4px;line-height:1.6">
    <div><svg width="5" height="5" viewBox="0 0 10 10" style="vertical-align:-.5px"><path d="M2 1h2l1 2-1.5 1a6 6 0 0 0 2.5 2.5L7 5l2 1v2l-1 1C4 9 1 6 1 2z" fill="#fff"/></svg> 555-010-2040</div>
    <div><svg width="5" height="5" viewBox="0 0 10 10" style="vertical-align:-.5px"><rect x="1" y="2" width="8" height="6" fill="#fff"/><path d="M1 2l4 3 4-3" fill="none" stroke="#222" stroke-width=".8"/></svg> hello@tundraline-example.com</div>
    <div><svg width="5" height="5" viewBox="0 0 10 10" style="vertical-align:-.5px"><path d="M5 9C2 6 2 4.5 2 4a3 3 0 0 1 6 0c0 .5 0 2-3 5z" fill="#fff"/><circle cx="5" cy="4" r="1" fill="#222"/></svg> 12 Icefield Road, Northridge, box 40210</div>
  </div>
  <div class="abs" style="left:11px;top:132px;color:#fff;font-size:6px;letter-spacing:1px">www.tundraline-example.com</div>
  <div class="logo light" style="right:12px;top:124px;font-size:12px">TUNDRALINE<small style="font-size:3.2px;letter-spacing:1.6px">FROZEN GROUND CONSULTING</small></div>
</section>

</body>
</html>
```